THE CRAFT LUMINARIES - Visionary Studios Who Elevate Design Into Fine Art.

Coffee-table book format.Will feature 20 'design' companies, one from each of 20 categories:3D Design . Branding Design . Broadcast Design . Communication . Digital Design Fashion . Exhibition Design . Furniture Design . Graphic Design . Industrial Design Interior Design . Jewelry . Lighting Design . Package Design . Retail Design . Sustainable Design . Urban Design . Web Design . Yacht DesignWant an eye-catching photo(s), design, etc. This will involve some creative effort.
Updates

After some thought, decided something that is a common thread through all design industries. A nice desk, upon which is a blank sketch pad, a pencil, and beside them a computer. A designer has a new idea, uses the sketch pad, then moves on to the computer to develop his/her idea. Cheers, Tobias

Target Market(s)

US professionals who own companies involved in the world of design.

Requirements
Must have
• Format is 11 in wide and 10 inches high cover.
• Photograph(s) or artwork that will catch the eye of the
• readers browsing the book sections.

```html
<!DOCTYPE html>
<html lang="en">
<head>
<meta charset="utf-8">
<title>The Craft Luminaries – Book Cover</title>
<link rel="stylesheet" href="https://fonts.googleapis.com/css2?family=Inter:wght@200;900&family=Oswald:wght@600&display=swap">
<style>
  :root {
    --paper: #ffffff;
    --ink: #0d0d0d;
    --ghost: #6a6a6a;
    --photo-light: #bdbdbd;
    --photo-mid: #7a7a7a;
    --photo-dark: #2b2b2b;
    --author: #f4f4f4;
    --subtitle: #f0f0f0;
  }
  html, body {
    margin: 0;
    padding: 0;
    width: 1200px;
    height: 859px;
    overflow: hidden;
    background: var(--paper);
  }
  .cover {
    position: relative;
    width: 1200px;
    height: 859px;
    overflow: hidden;
    background: var(--paper);
    font-family: "Inter", "Helvetica Neue", Arial, sans-serif;
  }
  .cover-photo {
    position: absolute;
    left: 0;
    top: 250px;
    width: 1200px;
    height: 609px;
    background:
      radial-gradient(ellipse at 78% 35%, #e6e6e6 0 14%, transparent 30%),
      radial-gradient(ellipse at 35% 45%, var(--photo-dark) 0 18%, transparent 40%),
      radial-gradient(ellipse at 30% 90%, var(--photo-light) 0 20%, transparent 45%),
      linear-gradient(160deg, var(--photo-mid) 0%, #4a4a4a 45%, #8c8c8c 100%);
  }
  .book-title {
    margin: 0;
    font-weight: 900;
  }
  .title-the {
    position: absolute;
    left: 30px;
    top: 30px;
    font-size: 140px;
    line-height: 1;
    letter-spacing: -0.06em;
    color: var(--ghost);
  }
  .title-main {
    position: absolute;
    left: 30px;
    top: 172px;
    font-size: 118px;
    line-height: 1;
    letter-spacing: -0.055em;
    color: var(--ink);
    white-space: nowrap;
  }
  .subtitle {
    position: absolute;
    left: 320px;
    top: 312px;
    margin: 0;
    font-weight: 200;
    font-size: 26px;
    line-height: 1.2;
    letter-spacing: 0.01em;
    color: var(--subtitle);
    white-space: nowrap;
  }
  .author {
    position: absolute;
    left: 660px;
    top: 600px;
    margin: 0;
    font-family: "Oswald", "Arial Narrow", sans-serif;
    font-weight: 600;
    font-size: 30px;
    line-height: 1.2;
    letter-spacing: 0.14em;
    color: var(--author);
    text-transform: uppercase;
  }
</style>
</head>
<body>
  <main class="cover">
    <div class="cover-photo" role="img" aria-label="Black and white overhead photo of a designer's desk with a coffee cup, sketch pad, pencil, keyboard and laptop"></div>
    <h1 class="book-title">
      <span class="title-the">the</span>
      <span class="title-main">Craft Luminaries</span>
    </h1>
    <p class="subtitle">Visionary Studios Who Elevate Design Into Fine Art</p>
    <p class="author">Dale Whitmore</p>
  </main>
</body>
</html>
```